Interactive Children's Media Book Company Website Design

We need a website DESIGN (no coding required) for a new interactive children's media book company called Tovira Studios.

We develop high-quality interactive children's books for the iPad/handheld device that seeks to delight and inspire young and old alike. Our stories are filled with heart and spirit, and we seek to breathe magic back into books so that people fall back in love with reading.

Tovira means "butterfly" in Korean. It plays on the idea that a caterpillar metamorphoses into a butterfly - and in the same way, our readers are transformed through the journey of experiencing our interactive books.

We're looking for something based on the ATTACHED LOGO DESIGN for our company. A website that's professional, modern, fun and inviting; easy to read and not-cluttered, but still portraying the feeling of innocence and childhood.

We're looking for something that resonates the magical experience we want to create for our readers. Specific requirements on pages, tabs, content, etc are below.

• There are 7 tabs on the Homepage of the website: HOME, OUR GRANDPA, ABOUT US, CAREERS, NEWS, CONTACT US, SHOP. (But there is an extra page called YOUR GRANDPA, which will be a sub-page under Our Grandpa).

HOME
• Would be great to have some key images of our book (3-4 screen shots) as the key focus of the homepage that automatically scroll through every few seconds. (Placeholder image attached). The images would link to the “Our Grandpa” page.
• Company logo (attached to brief) and slogan: “A new era of children’s media” quite prominent on page.
• Key text content to be on page: “Tovira means “butterfly” in Korean. Just as a caterpillar transforms into a butterfly, Tovira Studios takes the reader on an unforgettable journey of metamorphosis through our stories. We turn children’s books into a high-quality interactive experience on mobile platforms - breathing magic back into books, and inspiring people to fall back in love with reading. Through our unique characters full of heart and spirit, our stories delight and inspire young and old alike.”
• Skyline & social network Like & social network page link icons.
• Section on Latest News with a few of the latest entries.
• Section on latest sister images & comments that visitors have posted, which takes you to the “Your Grandpa” page.

OUR GRANDPA
• The title for this page is “Our Grandpa Hums at Breakfast Time”
• There will be a little iPad/handheld device icon (placeholder attached) for this book.
• There will be a link to the Pocketshelf to buy the app book.
• Key text content on this page: “Our debut interactive media book is coming soon on the iPad and handheld device! “Our Grandpa Hums at Breakfast Time” touches on the beautiful and inextricable (albeit sometimes frustrating!) bond between sisters.”
• There will be a section on “Features” which lists all the various special features the app book includes.
• There will be a YouTube clip embedded into the page, which shows how the app book works.
• A section that says: “Do you have a sister who’s not like other sisters? Share a photo and tell us about her!” which links to the sub-page “Your Grandpa”.
• Under this, there may be the most recent few images submitted by the public, which when clicked on, would also link to the sub-page “Your Grandpa”.

YOUR GRANDPA
• The main text on the page: “Do you have a sister who’s not like other sisters? Share a photo and tell us about her!”
• Main body of the page is a gallery of all the photos that have been submitted. If you click on each of the images, you get the comments that people have submitted with the photos.
• The page would also have a Submit Comments Form, where people can upload a picture of their sister(s) and write a comment to accompany the image.

ABOUT US
• Introductory text on page: “It was a chance conversation at Harbourline Terminal, where two friends discovered they shared a dream to create quality children's media. Both of them were excited by the possibilities of using new digital platforms to inspire and educate a younger generation. From that idea Tovira Studios was born. We seek to be the chrysalis of story telling - to inspire the hearts and minds of our generation, and generations to come.”
• Section to “Join the Mailing List” where they can put their email address in and submit.
• Bios of 2x people with photos (bios in word doc attached) (do not have photos yet).

CAREERS
• The main text on the page: “We are always on the lookout for talented people to join our team. If you are a writer, illustrator, animator, iOS/android developer, musician, creative-writing translator - or have something special to offer Tovira Studios - we are keen to hear from you. Send us a message through the Contact Us tab above.”

NEWS
• Regular News page, with blog-type entries.

CONTACT US
• Online submit Contact Us form
• The main text on page: “Our studio is based in the Ember Craft Cooperative, 43 Pukeora Street, Marangai, Wellington. Ember is a professional, creative collective - with four separate studios, gallery, and retail store. For more information on Ember, visit: http://www.embercraftco.example.nz”
• “We would love to hear from you! Whether you have questions, ideas, comments, or just want to say hullo - please leave us a message and we will get back to you soon.”
• Including image of the premises (Ember image attached to brief).

SHOP
• Where visitors can purchase merchandise (t-shirts, mugs, etc) of the book/company.

```html
<!DOCTYPE html>
<html lang="en">
<head>
<meta charset="utf-8">
<title>Tovira Studios – Our Grandpa Gallery</title>
<link href="https://fonts.googleapis.com/css2?family=Fredoka:wght@400;500;600&family=Gelasio&family=Arimo:wght@400;700&display=swap" rel="stylesheet">
<style>
:root{
  --sky:#cdeefa;
  --sky-deep:#9fdcf2;
  --navy:#25506b;
  --blue:#2e6bb5;
  --purple:#7a22c4;
  --purple-deep:#5b1aa0;
  --teal:#2a6470;
  --page:#f1f1f1;
  --footer:#1d1d1d;
  --cyan:#27b7e6;
  --grey-text:#8a8a8a;
  --white:#ffffff;
}
*{box-sizing:border-box;margin:0;padding:0}
html,body{width:1136px;height:1200px;overflow:hidden}
body{position:relative;background:var(--page);font-family:"Arimo",Arial,sans-serif}
.abs{position:absolute}

/* side scenery */
.scenery-left{left:0;top:92px;width:80px;height:1108px;background:linear-gradient(180deg,#7cc84a 0%,#c89a58 30%,#e8c070 60%,#f0b030 100%)}
.scenery-right{right:0;top:92px;width:82px;height:1108px;background:linear-gradient(180deg,#bfe6f7 0%,#d7eefa 40%,#f2c08a 70%,#7fc1ea 100%)}
.page{left:80px;top:92px;width:974px;height:906px;background:var(--page)}

/* header */
.site-header{left:0;top:0;width:1136px;height:92px;background:linear-gradient(180deg,#dcf4fd 0%,var(--sky) 85%,var(--sky-deep) 100%);border-bottom:3px solid #8fd0ea}
.brand{left:108px;top:18px;display:flex;align-items:center;gap:10px}
.brand-dot{width:36px;height:36px;border-radius:50%;background:var(--purple)}
.brand-name{font-family:"Fredoka",sans-serif;font-weight:500;font-size:30px;color:#5a5a5a;line-height:1}
.main-nav{left:378px;top:30px;display:flex;align-items:center;gap:0}
.main-nav a{font-family:"Fredoka",sans-serif;font-weight:500;font-size:17px;color:var(--navy);text-decoration:none;padding:6px 15px}
.main-nav a.is-active{background:var(--blue);color:var(--white);border-radius:22px;border:2px solid #1f4f8f}
.cart{left:956px;top:36px;display:flex;align-items:center;gap:6px;font-family:"Fredoka",sans-serif;font-weight:500;font-size:16px;color:var(--navy)}

/* intro */
.title-bar{left:71px;top:152px;width:463px;height:52px;background:linear-gradient(180deg,#6b6b6b,#2a2a2a);box-shadow:0 2px 4px rgba(0,0,0,.3);color:var(--white);font-family:"Fredoka",sans-serif;font-weight:500;font-size:22px;line-height:52px;padding-left:44px}
.intro{left:112px;top:226px;width:430px;font-family:"Gelasio",Georgia,serif;font-size:17px;line-height:23px;color:var(--teal)}
.device{left:627px;top:134px;width:391px;height:204px;border-radius:34px;background:#111;border:6px solid #e6e6e6;box-shadow:0 0 0 2px #333}
.device-screen{left:686px;top:148px;width:262px;height:176px;background:linear-gradient(180deg,#8ed0f2 0%,#6ab04a 70%,#3c8a2e 100%)}
.store-badge{left:715px;top:306px;width:204px;height:55px;background:linear-gradient(180deg,#a23ee6,var(--purple-deep));color:var(--white);font-family:"Fredoka",sans-serif;text-align:center;padding-top:5px}
.store-badge small{display:block;font-size:12px}
.store-badge strong{display:block;font-size:21px;font-weight:500;line-height:22px}
.store-glow{left:715px;top:362px;width:204px;height:40px;background:linear-gradient(180deg,rgba(162,62,230,.18),rgba(241,241,241,0))}

/* gallery */
.gallery-title{left:118px;top:416px;font-family:"Fredoka",sans-serif;font-weight:500;font-size:22px;color:var(--purple)}
.thumb{width:112px;height:73px;box-shadow:3px 3px 0 #d6d6d6}
.thumb.girl{background:linear-gradient(135deg,#e06a2a 0%,#f4a070 50%,#3a9a3a 100%)}
.thumb.yard{background:linear-gradient(180deg,#8ed0f2 0%,#6ab04a 60%,#c04030 100%)}
.caption{width:120px;display:flex;align-items:center;gap:4px;font-size:11px;color:var(--grey-text)}
.caption b{font-weight:400;color:var(--purple)}
.ico-like{width:12px;height:11px;border:1.5px solid var(--purple);border-radius:2px}
.ico-chat{width:12px;height:9px;border:1px solid #999;border-radius:3px}

/* modal */
.comment-modal{left:391px;top:417px;width:387px;height:234px;background:linear-gradient(180deg,#d9f5fd,#b4e6f7);border:4px solid #3d79c7;border-radius:4px}
.comment-modal h2{position:absolute;left:18px;top:16px;font-family:"Fredoka",sans-serif;font-weight:500;font-size:16px;color:var(--purple)}
.close{position:absolute;right:-8px;top:-6px;width:28px;height:28px;border-radius:50%;background:var(--blue);border:2px solid var(--white);color:var(--white);font:700 15px/24px Arial,sans-serif;text-align:center}
.field-label{position:absolute;font-family:"Fredoka",sans-serif;font-size:13.5px;color:var(--navy);text-align:right;width:100px}
.field{position:absolute;left:136px;width:235px;background:#e9f9ff;border:1px solid #9bcde4}
.browse{position:absolute;right:3px;top:3px;width:54px;height:18px;background:var(--blue);color:var(--white);font-size:10px;line-height:18px;text-align:center}
.submit{position:absolute;left:133px;top:184px;width:76px;height:30px;border-radius:16px;background:var(--blue);border:2px solid #1f4f8f;color:var(--white);font-family:"Fredoka",sans-serif;font-weight:500;font-size:14px;line-height:26px;text-align:center}

/* pager */
.pager{left:115px;top:866px;width:903px;height:43px;background:var(--white);box-shadow:2px 2px 0 #dcdcdc;display:flex;align-items:center;padding-left:24px;gap:16px;font-family:"Fredoka",sans-serif;font-size:14px;color:var(--blue)}
.pager .current{width:20px;height:20px;background:var(--purple-deep);color:var(--white);text-align:center;line-height:20px;font-size:11px}
.post-btn{left:815px;top:872px;width:195px;height:29px;background:linear-gradient(180deg,#3c82cf,#1f5aa8);border:1px solid #174c90;color:var(--white);font-family:"Fredoka",sans-serif;font-size:14px;line-height:27px;text-align:center}

/* footer */
.site-footer{left:80px;top:998px;width:974px;height:202px;background:var(--footer)}
.foot-head{font-family:"Fredoka",sans-serif;font-weight:500;font-size:17px;color:var(--cyan)}
.foot-links{list-style:none;font-size:12px;color:var(--white);line-height:20px}
.like-row{display:flex;align-items:center;gap:8px;font-size:11px;color:var(--white)}
.like-btn{background:#eef2f8;color:#2b4a8a;font-weight:700;padding:2px 6px;border:1px solid #9aa8c8}
.like-count{background:var(--white);color:#333;padding:2px 6px}
.social{display:flex;gap:10px}
.social span{width:20px;height:20px;border-radius:3px}
.rule{width:254px;height:1px;background:#444}
.blog-thumb{width:62px;height:62px;border:4px solid var(--white);background:linear-gradient(135deg,#9a9a9a,#3a3a3a)}
.blog-title{font-size:14px;color:var(--white)}
.blog-text{font-size:11.5px;color:#b5b5b5;line-height:14px}
.blog-meta{font-size:10px;color:var(--white);font-weight:700}
.blog-meta em{font-style:normal;color:#f0a020}
.blog-meta i{font-style:normal;color:var(--cyan)}
</style>
</head>
<body>

<div class="abs scenery-left" role="img" aria-label="Illustrated children's characters and garden scenery"></div>
<div class="abs scenery-right" role="img" aria-label="Illustrated child character against a soft sky"></div>
<div class="abs page"></div>

<header class="abs site-header">
  <div class="abs brand"><span class="brand-dot"></span><span class="brand-name">Tovira Studios</span></div>
  <nav class="abs main-nav">
    <a href="#">Home</a><a href="#" class="is-active">Our Grandpa</a><a href="#">About</a><a href="#">Careers</a><a href="#">Contact</a><a href="#">Shop</a>
  </nav>
  <div class="abs cart">
    <svg width="18" height="18" viewBox="0 0 18 18"><path d="M1 3h3l2 9h9l2-7H5" fill="none" stroke="#3a8a3a" stroke-width="2"/><circle cx="7" cy="15" r="1.6" fill="#3a8a3a"/><circle cx="14" cy="15" r="1.6" fill="#3a8a3a"/></svg>
    My Cart
  </div>
</header>

<h1 class="abs title-bar">Our Grandpa Hums at Breakfast Time</h1>
<p class="abs intro">Do you have a sister who’s not like other sisters? Share a photo and tell us about her!</p>

<div class="abs device"></div>
<div class="abs device-screen" role="img" aria-label="Book screenshot: girl on a trampoline in a backyard"></div>
<div class="abs store-badge"><small>Available on the</small><strong>POCKETSHELF</strong></div>
<div class="abs store-glow"></div>

<h2 class="abs gallery-title">Tovira Photos Gallery</h2>

<!-- row 1 -->
<div class="abs thumb girl" style="left:117px;top:470px" role="img" aria-label="Submitted photo"></div>
<div class="abs thumb yard" style="left:275px;top:470px" role="img" aria-label="Submitted photo"></div>
<div class="abs thumb girl" style="left:430px;top:470px" role="img" aria-label="Submitted photo"></div>
<div class="abs thumb girl" style="left:591px;top:470px" role="img" aria-label="Submitted photo"></div>
<div class="abs thumb yard" style="left:747px;top:470px" role="img" aria-label="Submitted photo"></div>
<div class="abs thumb girl" style="left:904px;top:470px" role="img" aria-label="Submitted photo"></div>
<div class="abs caption" style="left:118px;top:551px"><span class="ico-like"></span>|<span class="ico-chat"></span>Comment - <b>15</b></div>
<div class="abs caption" style="left:273px;top:551px"><span class="ico-like"></span>|<span class="ico-chat"></span>Comment - <b>02</b></div>
<div class="abs caption" style="left:748px;top:551px">Comment - <b>02</b></div>
<div class="abs caption" style="left:905px;top:551px"><span class="ico-like"></span>|<span class="ico-chat"></span>Comment - <b>15</b></div>

<!-- row 2 -->
<div class="abs thumb girl" style="left:117px;top:583px" role="img" aria-label="Submitted photo"></div>
<div class="abs thumb yard" style="left:275px;top:583px" role="img" aria-label="Submitted photo"></div>
<div class="abs thumb girl" style="left:430px;top:583px" role="img" aria-label="Submitted photo"></div>
<div class="abs thumb girl" style="left:591px;top:583px" role="img" aria-label="Submitted photo"></div>
<div class="abs thumb yard" style="left:747px;top:583px" role="img" aria-label="Submitted photo"></div>
<div class="abs thumb girl" style="left:904px;top:583px" role="img" aria-label="Submitted photo"></div>
<div class="abs caption" style="left:118px;top:664px"><span class="ico-like"></span>|<span class="ico-chat"></span>Comment - <b>15</b></div>
<div class="abs caption" style="left:273px;top:664px"><span class="ico-like"></span>|<span class="ico-chat"></span>Comment - <b>02</b></div>
<div class="abs caption" style="left:429px;top:664px"><span class="ico-like"></span>|<span class="ico-chat"></span>Comment - <b>25</b></div>
<div class="abs caption" style="left:590px;top:664px"><span class="ico-like"></span>|<span class="ico-chat"></span>Comment - <b>15</b></div>
<div class="abs caption" style="left:746px;top:664px"><span class="ico-like"></span>|<span class="ico-chat"></span>Comment - <b>02</b></div>
<div class="abs caption" style="left:905px;top:664px"><span class="ico-like"></span>|<span class="ico-chat"></span>Comment - <b>15</b></div>

<!-- row 3 -->
<div class="abs thumb girl" style="left:117px;top:692px" role="img" aria-label="Submitted photo"></div>
<div class="abs thumb yard" style="left:275px;top:692px" role="img" aria-label="Submitted photo"></div>
<div class="abs thumb girl" style="left:430px;top:692px" role="img" aria-label="Submitted photo"></div>
<div class="abs thumb girl" style="left:591px;top:692px" role="img" aria-label="Submitted photo"></div>
<div class="abs thumb yard" style="left:747px;top:692px" role="img" aria-label="Submitted photo"></div>
<div class="abs thumb girl" style="left:904px;top:692px" role="img" aria-label="Submitted photo"></div>
<div class="abs caption" style="left:118px;top:773px"><span class="ico-like"></span>|<span class="ico-chat"></span>Comment - <b>15</b></div>
<div class="abs caption" style="left:273px;top:773px"><span class="ico-like"></span>|<span class="ico-chat"></span>Comment - <b>02</b></div>
<div class="abs caption" style="left:429px;top:773px"><span class="ico-like"></span>|<span class="ico-chat"></span>Comment - <b>25</b></div>
<div class="abs caption" style="left:590px;top:773px"><span class="ico-like"></span>|<span class="ico-chat"></span>Comment - <b>15</b></div>
<div class="abs caption" style="left:746px;top:773px"><span class="ico-like"></span>|<span class="ico-chat"></span>Comment - <b>02</b></div>
<div class="abs caption" style="left:905px;top:773px"><span class="ico-like"></span>|<span class="ico-chat"></span>Comment - <b>15</b></div>

<!-- comment form -->
<section class="abs comment-modal">
  <h2>Post Your Comment</h2>
  <span class="close">✕</span>
  <span class="field-label" style="left:20px;top:69px">Name</span>
  <span class="field" style="top:62px;height:27px"></span>
  <span class="field-label" style="left:20px;top:102px">Upload Image</span>
  <span class="field" style="top:96px;height:27px"><span class="browse">Browse</span></span>
  <span class="field-label" style="left:20px;top:135px">Commet</span>
  <span class="field" style="top:131px;height:42px"></span>
  <span class="submit">Submit</span>
</section>

<!-- pagination -->
<nav class="abs pager">
  <svg width="18" height="20" viewBox="0 0 18 20"><path d="M17 0v20L0 10z" fill="#2e6bb5"/></svg>
  <span class="current">1</span><span>2</span><span>3</span><span>4</span><span>5 . . .</span>
  <svg width="18" height="20" viewBox="0 0 18 20"><path d="M1 0v20l17-10z" fill="#2e6bb5"/></svg>
</nav>
<div class="abs post-btn">Post Your Comments</div>

<!-- footer -->
<footer class="abs site-footer">
  <h3 class="abs foot-head" style="left:54px;top:38px">Tovira</h3>
  <ul class="abs foot-links" style="left:55px;top:66px">
    <li>Home</li><li>About us</li><li>Browse Books</li><li>Collections</li><li>Terms of Use</li><li>Privacy Policy</li>
  </ul>

  <h3 class="abs foot-head" style="left:215px;top:38px">Social Connectivity</h3>
  <div class="abs like-row" style="left:216px;top:65px"><span class="like-btn">Like</span><span class="like-count">12,922</span>people like this.</div>
  <div class="abs social" style="left:216px;top:98px">
    <span style="background:#3b5ea8"></span><span style="background:#34a6dd"></span><span style="background:#1f7ab8"></span><span style="background:#f07a1a"></span>
  </div>
  <div class="abs rule" style="left:216px;top:130px"></div>
  <p class="abs" style="left:215px;top:148px;font-size:12px;color:#fff">Copyright Tovira Studios ©2011</p>

  <h3 class="abs foot-head" style="left:509px;top:38px">Recent Blogs Posted</h3>
  <div class="abs blog-thumb" style="left:513px;top:70px" role="img" aria-label="Blog post photo"></div>
  <p class="abs blog-title" style="left:584px;top:72px">The Total Lunar Eclipse As Seen By Skyline Users</p>
  <p class="abs blog-text" style="left:586px;top:93px;width:360px">Lorem ipsum dolor sit amet, conse ctetur adipiscing elit. Aliquam Lorem ipsum dolor sit amet</p>
  <p class="abs blog-meta" style="left:588px;top:124px">Sept 10, 2011 &nbsp;•&nbsp; <em>NO COMMENTS</em> &nbsp;•&nbsp; <i>LEARN MORE</i></p>
</footer>

</body>
</html>
```